Corporate Hollowmere business cards to be handed to investor, bankers etc. Needs to have a young feel

I need business cards designed for a technology company that provides vanto-like rapid response on the security industry. I would like it simple but very cool and tasteful. See attached documents for artwork and colours to be used. Cut sheet describes business model. Card stock should be thicker than normal. I would like the one side to be just the art and the other to have the contact info with maybe the pin somewhere.

Target Market(s)

Investors

Industry/Entity Type

Business

Contact Information for Business Card

Would like the logo attached on one side with name address and other info on the other side.

Font styles to use
Other font styles liked:
• See existing logo

Colors
6b449b
886aae
e4daeb
ffffff

Requirements
Must have
• Name: Gregory Thalassides
• Address: 47 Orchard Lane, Toronto, On, L6R2C8
• Tel: 647-5550192
• Email: greg@hollowmere.io
Nice to have
• See logo colours

```html
<!DOCTYPE html>
<html lang="en">
<head>
<meta charset="utf-8">
<title>Hollowmere Business Card</title>
<link rel="stylesheet" href="https://fonts.googleapis.com/css2?family=Roboto:wght@400&family=Roboto+Condensed:wght@500&display=swap">
<style>
  :root {
    --backdrop: #9c9c9c;
    --card: #f4f4f4;
    --ink: #1c1a1e;
    --text: #4a4a4a;
    --brand-purple: #6b449b;
    --brand-lilac: #886aae;
  }
  * { margin: 0; padding: 0; box-sizing: border-box; }
  html, body {
    width: 1200px;
    height: 960px;
    overflow: hidden;
  }
  body {
    background: var(--backdrop);
    position: relative;
    font-family: "Roboto", Arial, sans-serif;
  }
  .card {
    position: absolute;
    left: 320px;
    width: 600px;
    height: 344px;
    background: var(--card);
  }
  .card--front { top: 102px; }
  .card--back { top: 492px; }

  .brand {
    position: absolute;
    left: 0;
    right: 0;
    top: 138px;
    display: flex;
    justify-content: center;
    align-items: center;
    gap: 14px;
  }
  .brand__dot {
    width: 34px;
    height: 34px;
    border-radius: 50%;
    background: var(--brand-lilac);
    margin-top: 6px;
  }
  .brand__name {
    font-family: "Roboto", Arial, sans-serif;
    font-weight: 400;
    font-size: 62px;
    line-height: 1;
    color: var(--ink);
    letter-spacing: -0.5px;
  }

  .contact {
    position: absolute;
    top: 140px;
    left: 0;
    right: 0;
    display: flex;
    justify-content: center;
  }
  .contact__identity {
    width: 282px;
    text-align: right;
    padding-right: 18px;
    border-right: 1.5px solid var(--brand-purple);
  }
  .contact__name {
    font-family: "Roboto Condensed", "Arial Narrow", sans-serif;
    font-weight: 500;
    font-size: 19px;
    line-height: 24px;
    color: var(--brand-purple);
  }
  .contact__address {
    font-size: 14.5px;
    line-height: 19px;
    color: var(--text);
    font-style: normal;
  }
  .contact__lines {
    width: 318px;
    padding-left: 18px;
    list-style: none;
    padding-top: 1px;
  }
  .contact__line {
    display: flex;
    align-items: center;
    gap: 7px;
    font-size: 14.5px;
    line-height: 19px;
    color: var(--text);
  }
  .contact__icon {
    width: 13px;
    height: 13px;
    fill: var(--brand-purple);
    flex: none;
  }
</style>
</head>
<body>
  <section class="card card--front">
    <div class="brand">
      <span class="brand__dot"></span>
      <span class="brand__name">hollowmere</span>
    </div>
  </section>

  <section class="card card--back">
    <div class="contact">
      <div class="contact__identity">
        <div class="contact__name">Gregory Thalassides</div>
        <address class="contact__address">47 Orchard Lane<br>Toronto, On, L6R2C8</address>
      </div>
      <ul class="contact__lines">
        <li class="contact__line">
          <svg class="contact__icon" viewBox="0 0 16 16" aria-hidden="true"><path d="M3.6 1.2 6 3.6c.4.4.4 1 0 1.4L4.9 6.1a9 9 0 0 0 5 5l1.1-1.1c.4-.4 1-.4 1.4 0l2.4 2.4c.4.4.4 1 0 1.4l-1.2 1.2C11 16.5 -.5 5 1 2.4l1.2-1.2c.4-.4 1-.4 1.4 0z"/></svg>
          647-5550192
        </li>
        <li class="contact__line">
          <svg class="contact__icon" viewBox="0 0 16 16" aria-hidden="true"><path d="M1 3h14v10H1z M1.8 3.8 8 8.6l6.2-4.8" stroke="#f4f4f4" stroke-width="1.2"/></svg>
          greg@hollowmere.io
        </li>
        <li class="contact__line">
          <svg class="contact__icon" viewBox="0 0 16 16" aria-hidden="true"><circle cx="8" cy="8" r="7"/><path d="M4 4.5c1.5 0 2 1 1.5 2S7 8 6 9.5s-2 .5-2.5-.5M10 3c-.5 1.5 1 2 2 2.5M9 12.5c.5-1.5 2.5-2 3-1" stroke="#f4f4f4" stroke-width="1.1" fill="none"/></svg>
          www.hollowmere.io
        </li>
      </ul>
    </div>
  </section>
</body>
</html>
```